business card for a shoe shop

we would like a business card for a family owned shoe shop.
With this information included.
Darnell's Shoe Store
Family owned since 1947

then on other side
Darnell's Shoe Store
Footwear fitting specialist
Phone: 9187 2630
218 Quarry St, Fernleigh Downs 3187
(cnr. Hartwick Rd and Quarry St)
darnellshoes218@examplemail.com
if could incorporate the purple color on card i have attached.

```html
<!DOCTYPE html>
<html lang="en">
<head>
<meta charset="utf-8">
<title>Darnell's Shoe Store – Business Card</title>
<link rel="stylesheet" href="https://fonts.googleapis.com/css2?family=Lato:wght@400;700&family=Open+Sans:wght@400&family=Poppins:wght@300;400&display=swap">
<style>
  :root {
    --page-bg: #efefef;
    --brand-purple: #964cff;
    --brand-purple-deep: #8a45ec;
    --ink-purple: #8750ea;
    --panel-white: #ffffff;
    --photo-light: #e4f4f3;
    --photo-mid: #c9dedd;
  }
  * { box-sizing: border-box; margin: 0; padding: 0; }
  html, body {
    width: 1200px;
    height: 958px;
    overflow: hidden;
    background: var(--page-bg);
  }
  .canvas {
    position: relative;
    width: 1200px;
    height: 958px;
  }
  .card {
    position: absolute;
    left: 328px;
    width: 552px;
    height: 331px;
    border-radius: 22px;
    overflow: hidden;
    background: var(--brand-purple);
  }
  .card--front { top: 126px; }
  .card--back { top: 523px; }

  .shoe-photo {
    position: absolute;
    border-radius: 50%;
    background: radial-gradient(circle at 40% 35%, var(--photo-light), var(--photo-mid));
  }
  .shoe-photo--left { left: 58px; top: 74px; width: 204px; height: 204px; }
  .shoe-photo--right { left: 364px; top: 5px; width: 190px; height: 190px; }

  .front-title {
    position: absolute;
    right: 14px;
    top: 270px;
    font-family: "Lato", sans-serif;
    font-weight: 700;
    font-size: 28px;
    letter-spacing: -1px;
    line-height: 1;
    color: var(--panel-white);
    text-align: right;
  }
  .front-tagline {
    position: absolute;
    right: 15px;
    top: 296px;
    font-family: "Lato", sans-serif;
    font-weight: 400;
    font-size: 14px;
    letter-spacing: -0.2px;
    line-height: 1;
    color: var(--panel-white);
  }

  .back-panel {
    position: absolute;
    left: 24px;
    top: 18px;
    width: 506px;
    height: 295px;
    border-radius: 14px;
    background: var(--panel-white);
    text-align: center;
    color: var(--ink-purple);
  }
  .back-title {
    position: absolute;
    left: 0; right: 0;
    top: 32px;
    font-family: "Poppins", sans-serif;
    font-weight: 400;
    font-size: 35px;
    line-height: 1;
  }
  .back-specialty {
    position: absolute;
    left: 0; right: 0;
    top: 92px;
    font-family: "Open Sans", sans-serif;
    font-weight: 400;
    font-size: 22px;
    line-height: 1;
  }
  .back-contact {
    position: absolute;
    left: 0; right: 0;
    top: 154px;
    font-family: "Poppins", sans-serif;
    font-weight: 300;
    font-size: 17px;
    letter-spacing: 1px;
    line-height: 26.7px;
    list-style: none;
  }
</style>
</head>
<body>
<main class="canvas">
  <section class="card card--front">
    <div class="shoe-photo shoe-photo--left" role="img" aria-label="Photo of a navy canvas sneaker and a tan lace-up shoe on a pale circular backdrop"></div>
    <div class="shoe-photo shoe-photo--right" role="img" aria-label="Photo of a grey suede sneaker and a brown leather sneaker on a pale circular backdrop"></div>
    <h1 class="front-title">DARNELL'S SHOE STORE</h1>
    <p class="front-tagline">Family owned since 1947</p>
  </section>

  <section class="card card--back">
    <div class="back-panel">
      <h2 class="back-title">Darnell's Shoe Store</h2>
      <p class="back-specialty">Footwear fitting specialist</p>
      <ul class="back-contact">
        <li>Phone: 9187 2630</li>
        <li>218 Quarry St, Fernleigh Downs 3187</li>
        <li>(cnr. Hartwick Rd and Quarry St)</li>
        <li>darnellshoes218@examplemail.com</li>
      </ul>
    </div>
  </section>
</main>
</body>
</html>
```